brightwell - Property Management DL Card

I am after a savvy designer to cut through junk mail! so many real estate agents use flyers to promote themselves and their business and usually sales. We are a property management firm (residential) and we want to represent landlords that have existing investment properties and need a quality agent to represent them. Can you help?
DL size, will be printed and delivered to mailboxes. For a look at our website go to www.brightwellhx.com.au. Keep it simple and clutter free.
it is to be double sided - with one side to be simple and clear - just our website, logo and telephone number on the back.
attached is our logo and our telephone number is 1300 82 41 96
the above are 2 essential elements to be included + our email address: admin@brightwellhx.com.au
also attached are our transparent price list

Target Market(s)
property investors,
people that manage properties themselves
Industry/Entity Type
Property Management
Other font styles liked:
- arial
Look and feel

```html
<!DOCTYPE html>
<html lang="en">
<head>
<meta charset="utf-8">
<title>brightwell – Property Management DL Card</title>
<link href="https://fonts.googleapis.com/css2?family=Open+Sans:wght@300;400&display=swap" rel="stylesheet">
<style>
  :root {
    --page-bg: #d9d9d9;
    --sand: #e0d7b8;
    --ink: #0a0a0c;
    --black: #000000;
    --rust: #c43f28;
    --rust-text: #f2c3b2;
    --white: #ffffff;
    --grey-tag: #9a9a9a;
    --phone-red: #c9452d;
  }
  * { margin: 0; padding: 0; box-sizing: border-box; }
  html, body {
    width: 1200px; height: 1200px; overflow: hidden;
    background: var(--page-bg);
    font-family: "Open Sans", Arial, sans-serif;
  }
  .canvas { position: relative; width: 1200px; height: 1200px; }

  /* Front side */
  .card-front {
    position: absolute; left: 118px; top: 56px; width: 1002px; height: 500px;
  }
  .top-band { position: absolute; left: 0; top: 0; width: 100%; height: 66px; background: var(--sand); }
  .hero-photo {
    position: absolute; left: 0; top: 66px; width: 719px; height: 361px;
    background: linear-gradient(180deg, #9a8a6a 0%, #a7733e 45%, #6b4a30 70%, #5a4a48 100%);
  }
  .brand-panel {
    position: absolute; left: 719px; top: 66px; width: 283px; height: 361px;
    background: var(--ink);
  }
  .brand {
    position: absolute; font-weight: 300; color: var(--white); line-height: 1;
  }
  .brand-name { display: block; }
  .brand-tag { display: block; color: var(--grey-tag); }
  .brand-panel .brand { left: 60px; top: 160px; }
  .brand-panel .brand-name { font-size: 40px; letter-spacing: 0.5px; }
  .brand-panel .brand-tag { font-size: 17px; margin-top: 4px; padding-left: 6px; }

  .benefit-band {
    position: absolute; left: 0; top: 427px; width: 100%; height: 73px;
    background: var(--rust); color: var(--white);
  }
  .specialty {
    position: absolute; left: 70px; top: 21px; font-size: 21px; color: var(--rust-text);
  }
  .band-divider {
    position: absolute; left: 423px; top: 17px; width: 2px; height: 37px; background: var(--rust-text); opacity: .7;
  }
  .benefits { position: absolute; top: 15px; list-style: none; font-size: 16px; line-height: 21px; }
  .benefits li::before { content: "•"; margin-right: 7px; }
  .benefits-a { left: 448px; }
  .benefits-b { left: 714px; }

  /* Back side */
  .card-back {
    position: absolute; left: 119px; top: 637px; width: 1000px; height: 500px;
    background: var(--black); color: var(--white);
  }
  .card-back .brand { left: 56px; top: 48px; }
  .card-back .brand-name { font-size: 44px; letter-spacing: 0.5px; }
  .card-back .brand-tag { font-size: 19px; margin-top: 2px; padding-left: 7px; }
  .contact {
    position: absolute; left: 557px; top: 380px; padding-left: 22px;
    border-left: 2px solid #777; font-size: 18px; line-height: 24px; letter-spacing: 0.8px;
  }
  .contact .phone { color: var(--phone-red); }
</style>
</head>
<body>
<div class="canvas">
  <section class="card-front">
    <div class="top-band"></div>
    <div class="hero-photo" role="img" aria-label="Photo of a sunlit lounge with two orange armchairs, a low coffee table and a potted bamboo plant"></div>
    <div class="brand-panel">
      <div class="brand"><span class="brand-name">brightwell</span><span class="brand-tag">property group</span></div>
    </div>
    <div class="benefit-band">
      <p class="specialty">Property Management specialists</p>
      <div class="band-divider"></div>
      <ul class="benefits benefits-a">
        <li>Excellent communication</li>
        <li>Minimal vacancy</li>
      </ul>
      <ul class="benefits benefits-b">
        <li>No hidden extras</li>
        <li>The best rent return</li>
      </ul>
    </div>
  </section>

  <section class="card-back">
    <div class="brand"><span class="brand-name">brightwell</span><span class="brand-tag">property group</span></div>
    <div class="contact">
      <p class="phone">1 300 82 41 96</p>
      <p>PO Box C592, Harbourview NSW, 2199</p>
      <p>admin@brightwellhx.com.au</p>
    </div>
  </section>
</div>
</body>
</html>
```